"Oral Surgery Office needs a Business Card Design with Logo"

We need a logo design and business card. The name of the office is Halvering Oral Surgery & Implant Center. The final design should communicate uniqueness as well as highly class office. The business card should emphasize power. I included the current business card below. Please design something unique

Target Market(s)

Dentists & Patients

Industry/Entity Type

Dental

Contact Information for Business Card

Unique Design to show success, prestige, Style, unmatched performance

Font styles to use
Serif

Colors
1b1b1b
ffffff
0556a4

Requirements
Must have
• Bussiness Name, Doctor's Name, Website, phone and Fax, email, office address
• Color should be either Black and White or Blue and White
Nice to have
• Clean look
Should not have
• the business card shouldn't be too busy. I feel like the old business card was too busy

```html
<!DOCTYPE html>
<html lang="en">
<head>
<meta charset="utf-8">
<title>Halvering Oral Surgery &amp; Implant Center – Business Card</title>
<link href="https://fonts.googleapis.com/css2?family=Tinos:wght@400;700&display=swap" rel="stylesheet">
<style>
  :root {
    --ink: #1b1b1b;
    --black: #000000;
    --paper: #ffffff;
    --muted: #444444;
    --stage: #4d4d4d;
    --shadow: rgba(0,0,0,0.45);
  }
  * { margin: 0; padding: 0; box-sizing: border-box; }
  html, body { width: 900px; height: 1200px; overflow: hidden; }
  body {
    background: var(--stage);
    font-family: "Tinos", "Times New Roman", serif;
    position: relative;
    color: var(--ink);
  }
  .card {
    position: absolute;
    left: 110px;
    width: 673px;
    height: 395px;
    border-radius: 22px;
    overflow: hidden;
    box-shadow: 0 4px 14px var(--shadow);
  }
  .card--front { top: 173px; background: var(--paper); }
  .card--back { top: 630px; background: var(--black); }

  .brand { position: absolute; display: flex; align-items: center; }
  .brand__mark { flex: none; border-radius: 50%; border: 7px solid currentColor; }
  .brand__name { text-transform: uppercase; font-weight: 400; line-height: 1; letter-spacing: 0.5px; }
  .brand__line1 { display: block; font-size: 32px; }
  .brand__line2 { display: block; font-size: 19px; margin-top: 8px; }

  .card--front .brand { left: 43px; top: 32px; color: var(--ink); }
  .card--front .brand__mark { width: 100px; height: 100px; margin-right: 17px; }

  .card--back .brand { left: 128px; top: 148px; color: var(--paper); }
  .card--back .brand__mark { width: 99px; height: 99px; margin-right: 16px; }
  .card--back .brand__line1 { font-size: 33px; }

  .doctor { position: absolute; left: 43px; top: 190px; }
  .doctor__name { font-size: 20px; font-weight: 700; }
  .doctor__title { font-size: 15px; color: var(--muted); margin-top: 1px; }

  .rule { position: absolute; left: 43px; right: 46px; top: 241px; height: 2px; background: var(--ink); }

  .contacts { position: absolute; left: 43px; top: 254px; list-style: none; font-size: 14.5px; }
  .contacts li { display: flex; align-items: center; height: 21px; }
  .contacts svg { width: 13px; height: 13px; margin-right: 10px; fill: var(--ink); }

  .address { position: absolute; right: 44px; top: 254px; text-align: right; font-size: 14.5px; line-height: 19.5px; font-style: normal; }

  .social-band {
    position: absolute; left: 0; right: 0; bottom: 0; height: 47px;
    background: var(--black); color: var(--paper);
    display: flex; align-items: center; padding-left: 43px; font-size: 14.5px;
  }
  .social { display: flex; align-items: center; margin-right: 28px; }
  .social__square { width: 19px; height: 19px; background: #8a8a8a; border-radius: 3px; margin-right: 10px; }
</style>
</head>
<body>
  <section class="card card--front">
    <div class="brand">
      <span class="brand__mark"></span>
      <span class="brand__name">
        <span class="brand__line1">Halvering Oral</span>
        <span class="brand__line2">Surgery &amp; Implant Center</span>
      </span>
    </div>

    <div class="doctor">
      <p class="doctor__name">DR. Marcus Delaney, D.D.S.</p>
      <p class="doctor__title">oral &amp; Maxillofacial Surgery</p>
    </div>

    <div class="rule"></div>

    <ul class="contacts">
      <li><svg viewBox="0 0 16 16"><path d="M3.5 1l2.5 3-1.5 2c1 2 2.5 3.5 4.5 4.5l2-1.5 3 2.5-1.5 2.5C7 14 2 9 1 3z"/></svg>555-210-4700</li>
      <li><svg viewBox="0 0 16 16"><path d="M4 1h8v4H4zM1 6h14v6h-3v3H4v-3H1zM5 10v4h6v-4z"/></svg>555-210-5006</li>
      <li><svg viewBox="0 0 16 16"><path d="M1 3h14v10H1zM2 4l6 5 6-5v-.5H2z" fill-rule="evenodd"/></svg>HalveringOralsurgeon@mailbox.com</li>
      <li><svg viewBox="0 0 16 16"><path d="M8 1a7 7 0 1 0 0 14A7 7 0 0 0 8 1zm0 1.3c.8.9 1.5 2.3 1.7 4H6.3C6.5 4.6 7.2 3.2 8 2.3zM2.4 7.3h2.6c0 1.4.3 2.6.8 3.7a5.7 5.7 0 0 1-3.4-3.7zm0 1.4zm11.2-.7a5.7 5.7 0 0 1-3.4 4.4c.5-1.1.8-2.3.8-3.7zM6.3 8.7h3.4c-.2 1.7-.9 3.1-1.7 4-.8-.9-1.5-2.3-1.7-4z"/></svg>www.halveringoralsurgerycenter.com</li>
    </ul>

    <address class="address">2840 Avenue K<br>Halvering, NY 10482</address>

    <div class="social-band">
      <span class="social"><span class="social__square"></span>halveringoral</span>
      <span class="social"><span class="social__square"></span>Halvering oral surgery &amp; implant Center</span>
    </div>
  </section>

  <section class="card card--back">
    <div class="brand">
      <span class="brand__mark"></span>
      <span class="brand__name">
        <span class="brand__line1">Halvering Oral</span>
        <span class="brand__line2">Surgery &amp; Implant Center</span>
      </span>
    </div>
  </section>
</body>
</html>
```